brindlewood carpentry business card 2.0

id like to get some extra info added to my current business card ,but i am also open to a new design as well ,id like it to be a clean professional look
i have attached the original card files, i have also attached the ridgemark guild logo and licensed builder logo that id like to add to all the current info on the old card
also the color green is important as seen in the company logo

Industry/Entity Type

Carpentry

Colors
9bcb3c

```html
<!DOCTYPE html>
<html lang="en">
<head>
<meta charset="utf-8">
<title>Brindlewood Carpentry – Business Card</title>
<link rel="stylesheet" href="https://fonts.googleapis.com/css2?family=Arimo:wght@400;700&display=swap">
<style>
  :root {
    --backdrop: #e4e4e2;
    --card: #2b2b2b;
    --card-edge: #9bcb3c;
    --green: #9bcb3c;
    --text-light: #e6e6e6;
    --rule: #5a5a5a;
    --badge-blue: #1f4e8c;
    --badge-yellow: #f3c318;
  }
  * { box-sizing: border-box; margin: 0; padding: 0; }
  html, body { width: 1200px; height: 801px; overflow: hidden; }
  body {
    background: var(--backdrop);
    font-family: "Arimo", Arial, sans-serif;
    position: relative;
  }
  .card {
    position: absolute;
    top: 240px;
    width: 520px;
    height: 300px;
    background: var(--card);
    border-bottom: 4px solid var(--card-edge);
    border-left: 2px solid var(--card-edge);
    overflow: hidden;
  }
  .card--front { left: 50px; }
  .card--back { left: 630px; }

  /* front */
  .licence-badge {
    position: absolute;
    left: 80px; top: 42px;
    width: 130px; height: 130px;
    border-radius: 50%;
    background: var(--green);
    border: 6px solid var(--text-light);
  }
  .holder {
    position: absolute;
    left: 48px; top: 196px;
  }
  .holder__name {
    color: var(--green);
    font-weight: 700;
    font-size: 22px;
    letter-spacing: 0.5px;
  }
  .holder__role {
    color: var(--text-light);
    font-size: 17px;
    margin-top: 4px;
  }
  .divider {
    position: absolute;
    left: 262px; top: 150px;
    width: 1px; height: 60px;
    background: var(--rule);
  }
  .contacts {
    position: absolute;
    left: 282px; top: 140px;
    list-style: none;
    color: var(--text-light);
    font-size: 13px;
  }
  .contacts li { display: flex; align-items: center; gap: 8px; height: 24px; }
  .contacts svg { width: 12px; height: 12px; flex: none; }
  .contacts .accent { color: var(--green); }

  /* back */
  .licence-badge--small {
    left: auto; right: 34px; top: 22px;
    width: 96px; height: 96px;
    border-width: 4px;
  }
  .guild-badge {
    position: absolute;
    right: 48px; top: 150px;
    width: 96px; height: 74px;
    background: var(--badge-blue);
  }
  .hero-scene {
    position: absolute;
    left: 40px; top: 90px;
    width: 300px; height: 300px;
    border-radius: 50%;
    background: radial-gradient(circle at 70% 20%, #6e6e6e 0%, #3a3a3a 45%, #262626 100%);
  }
</style>
</head>
<body>
  <section class="card card--front" aria-label="Business card front">
    <div class="licence-badge" role="img" aria-label="Licensed builder certification badge"></div>
    <div class="holder">
      <p class="holder__name">MARCUS HALE</p>
      <p class="holder__role">director brindlewood carpentry ltd</p>
    </div>
    <div class="divider"></div>
    <ul class="contacts">
      <li>
        <svg viewBox="0 0 12 12" aria-hidden="true"><path d="M2 1l2.5 0 1 3-1.5 1a6 6 0 0 0 3 3l1-1.5 3 1V11.5C6 11.5 .5 6 .5 1z" fill="var(--green)"/></svg>
        02104518876
      </li>
      <li>
        <svg viewBox="0 0 12 12" aria-hidden="true"><rect x="1" y="2.5" width="10" height="7" fill="none" stroke="var(--green)" stroke-width="1.2"/><path d="M1 2.5l5 4 5-4" fill="none" stroke="var(--green)" stroke-width="1.2"/></svg>
        marcus@brindlewoodcarpentry.conz
      </li>
      <li>
        <svg viewBox="0 0 12 12" aria-hidden="true"><circle cx="6" cy="6" r="5" fill="none" stroke="var(--green)" stroke-width="1.2"/><path d="M1 6h10M6 1c-3 3-3 7 0 10M6 1c3 3 3 7 0 10" fill="none" stroke="var(--green)" stroke-width="1"/></svg>
        <span>www.<span class="accent">brindlewoodcarpentry</span>.conz</span>
      </li>
    </ul>
  </section>

  <section class="card card--back" aria-label="Business card back">
    <div class="hero-scene" role="img" aria-label="Embossed illustration of houses and buildings in a circle"></div>
    <div class="licence-badge licence-badge--small" role="img" aria-label="Licensed builder certification badge"></div>
    <div class="guild-badge" role="img" aria-label="Ridgemark Guild membership badge"></div>
  </section>
</body>
</html>
```